Packaging for new retail dips "Quellmor"

* We require packaging for our new retail dip range.
* We have a small "Our Story" write up that we would like somewhere...
* We have approx. 7 different flavours - Hommous, Mediterranean Olive, Beetroot, Tzatziki etc. We would like one design where we can change the colour panel and the name of the dip.
* We are looking for a modern, clean, gourmet looking design - not the usual dip packaging you see on supermarket shelves.
* See my inspiration photo's.
* The Dieline attached is to scale.
Updates
Project Deadline Extended
Reason: Extension due to Dielines and Measurements not uploaded when we thought they were.
Target Market(s)
Will be going into retail supermarkets.
Industry/Entity Type
Retail
Font styles to use
Colors
Designer to choose colors to be used in the design.
Requirements
Must have
- * Please use our 'Quellmor' logo on the front and on the front side (if possible).
Nice to have
- * 'taste is everything' somewhere...
Should not have
- * No photo's of dips or photo's in general.

```html
<!DOCTYPE html>
<html lang="en">
<head>
<meta charset="utf-8">
<title>Quellmor Dip Packaging</title>
<link rel="stylesheet" href="https://fonts.googleapis.com/css2?family=Lobster&family=Montserrat:wght@300;400&display=swap">
<style>
  :root{
    --bg-top:#f7f7f8;
    --bg-bottom:#dcdce0;
    --ink:#333333;
    --white:#ffffff;
    --hommous-light:#a5d65d;
    --hommous-dark:#57641f;
    --olive-light:#ffb300;
    --olive-dark:#9c5b14;
    --beet-light:#d6146a;
    --beet-dark:#8b0d4f;
    --sans:'Montserrat', sans-serif;
    --script:'Lobster', cursive;
  }
  html,body{margin:0;padding:0;overflow:hidden;}
  .canvas{
    position:relative;width:1200px;height:1200px;overflow:hidden;
    background:linear-gradient(180deg,var(--bg-top),var(--bg-bottom));
    font-family:var(--sans);
  }
  .brand-mark{
    position:absolute;left:945px;top:160px;
    font-family:var(--sans);font-weight:300;font-size:32px;letter-spacing:3px;color:var(--ink);
    white-space:nowrap;
  }
  .label{position:absolute;display:block;filter:drop-shadow(0 8px 14px rgba(0,0,0,.18));}
  .label--main{left:320px;top:40px;width:560px;height:529px;}
  .side-panel{position:absolute;left:320px;top:585px;width:560px;height:220px;filter:drop-shadow(0 8px 14px rgba(0,0,0,.18));}
  .label--small{top:880px;width:292px;height:276px;}
  .label--main,.side-panel,.label--hommous{--light:var(--hommous-light);--dark:var(--hommous-dark);}
  .label--hommous{left:128px;}
  .label--olive{left:470px;--light:var(--olive-light);--dark:var(--olive-dark);}
  .label--beet{left:810px;--light:var(--beet-light);--dark:var(--beet-dark);}

  .panel-white{fill:var(--white);}
  .panel-light{fill:var(--light);}
  .panel-dark{fill:var(--dark);}
  .seal{fill:var(--white);stroke:var(--dark);stroke-width:1.5;}
  .seal-name{font-family:var(--sans);font-weight:300;font-size:16px;letter-spacing:1.5px;fill:var(--ink);text-anchor:middle;}
  .slogan{font-family:var(--script);font-size:17px;}
  .slogan-dark{fill:var(--dark);}
  .slogan-light{fill:var(--white);}
  .product-name{font-family:var(--sans);font-weight:400;font-size:19px;letter-spacing:2.5px;fill:var(--white);text-anchor:middle;}
  .product-sub{font-family:var(--script);font-size:12px;fill:var(--white);text-anchor:middle;}
  .product-uses{font-family:var(--sans);font-weight:300;font-size:8px;letter-spacing:.8px;fill:rgba(255,255,255,.8);text-anchor:middle;}
  .weight{font-family:var(--sans);font-weight:300;font-size:14px;fill:var(--dark);}
  .flavour{font-family:var(--sans);font-weight:400;font-size:11px;fill:var(--white);text-anchor:end;}
  .story-title{font-family:var(--script);font-size:30px;}
  .story-body{font-family:var(--sans);font-weight:300;font-size:12px;fill:var(--ink);}
  .side-seal{fill:var(--white);stroke:var(--ink);stroke-width:1.2;}
</style>
</head>
<body>
<div class="canvas">

  <div class="brand-mark">QUELLMOR</div>

  <svg class="label label--main" viewBox="0 0 365 345" aria-label="Taramasalata Hommous flavour lid">
    <rect class="panel-white" width="365" height="345"/>
    <polygon class="panel-light" points="290,0 365,0 365,218 148,218"/>
    <circle class="seal" cx="182" cy="108" r="70"/>
    <text class="seal-name" x="182" y="124">QUELLMOR</text>
    <g transform="rotate(-12 182 192)">
      <text class="slogan slogan-dark" x="92" y="200">taste is</text>
      <text class="slogan slogan-light" x="172" y="200">everything</text>
    </g>
    <rect class="panel-dark" y="226" width="365" height="70"/>
    <text class="product-name" x="182" y="252">TARAMASALATA</text>
    <text class="product-sub" x="182" y="270">Caviar Dip</text>
    <text class="product-uses" x="182" y="286">spread . sauce . dressing</text>
    <polygon class="panel-light" points="82,304 365,304 365,345 58,345"/>
    <text class="weight" x="12" y="330">150g</text>
    <text class="flavour" x="355" y="329">Hommous Flavor</text>
  </svg>

  <svg class="side-panel" viewBox="0 0 560 220" aria-label="Our Story side panel">
    <rect class="panel-white" width="560" height="220"/>
    <polygon class="panel-light" points="150,0 560,0 560,62 100,62"/>
    <text class="story-title" x="24" y="100"><tspan fill="var(--dark)">Our </tspan><tspan fill="var(--light)">Story</tspan></text>
    <text class="story-body" x="24" y="128">Lorem ipsum dolor sit amet, consectetur</text>
    <text class="story-body" x="24" y="145">adipiscing elit, sed do eiusmod tempor</text>
    <text class="story-body" x="24" y="162">incididunt ut labore et dolore magna aliqua.</text>
    <text class="story-body" x="24" y="179">Elementum nisi quis eleifend quam. Eu mi</text>
    <text class="story-body" x="24" y="196">bibendum neque egestas.</text>
    <circle class="side-seal" cx="460" cy="130" r="64"/>
    <text class="seal-name" x="460" y="145" style="font-size:15px">QUELLMOR</text>
  </svg>

  <svg class="label label--small label--hommous" viewBox="0 0 365 345" aria-label="Hommous flavour label">
    <rect class="panel-white" width="365" height="345"/>
    <polygon class="panel-light" points="290,0 365,0 365,218 148,218"/>
    <circle class="seal" cx="182" cy="108" r="70"/>
    <text class="seal-name" x="182" y="124">QUELLMOR</text>
    <g transform="rotate(-12 182 192)">
      <text class="slogan slogan-dark" x="92" y="200">taste is</text>
      <text class="slogan slogan-light" x="172" y="200">everything</text>
    </g>
    <rect class="panel-dark" y="226" width="365" height="70"/>
    <text class="product-name" x="182" y="252">TARAMASALATA</text>
    <text class="product-sub" x="182" y="270">Caviar Dip</text>
    <text class="product-uses" x="182" y="286">spread . sauce . dressing</text>
    <polygon class="panel-light" points="82,304 365,304 365,345 58,345"/>
    <text class="weight" x="12" y="330">150g</text>
    <text class="flavour" x="355" y="329">Hommous Flavor</text>
  </svg>

  <svg class="label label--small label--olive" viewBox="0 0 365 345" aria-label="Mediterranean Olive flavour label">
    <rect class="panel-white" width="365" height="345"/>
    <polygon class="panel-light" points="290,0 365,0 365,218 148,218"/>
    <circle class="seal" cx="182" cy="108" r="70"/>
    <text class="seal-name" x="182" y="124">QUELLMOR</text>
    <g transform="rotate(-12 182 192)">
      <text class="slogan slogan-dark" x="92" y="200">taste is</text>
      <text class="slogan slogan-light" x="172" y="200">everything</text>
    </g>
    <rect class="panel-dark" y="226" width="365" height="70"/>
    <text class="product-name" x="182" y="252">TARAMASALATA</text>
    <text class="product-sub" x="182" y="270">Caviar Dip</text>
    <text class="product-uses" x="182" y="286">spread . sauce . dressing</text>
    <polygon class="panel-light" points="82,304 365,304 365,345 58,345"/>
    <text class="weight" x="12" y="330">150g</text>
    <text class="flavour" x="355" y="329">Mediterranean Olive Flavor</text>
  </svg>

  <svg class="label label--small label--beet" viewBox="0 0 365 345" aria-label="Beetroot flavour label">
    <rect class="panel-white" width="365" height="345"/>
    <polygon class="panel-light" points="290,0 365,0 365,218 148,218"/>
    <circle class="seal" cx="182" cy="108" r="70"/>
    <text class="seal-name" x="182" y="124">QUELLMOR</text>
    <g transform="rotate(-12 182 192)">
      <text class="slogan slogan-dark" x="92" y="200">taste is</text>
      <text class="slogan slogan-light" x="172" y="200">everything</text>
    </g>
    <rect class="panel-dark" y="226" width="365" height="70"/>
    <text class="product-name" x="182" y="252">TARAMASALATA</text>
    <text class="product-sub" x="182" y="270">Caviar Dip</text>
    <text class="product-uses" x="182" y="286">spread . sauce . dressing</text>
    <polygon class="panel-light" points="82,304 365,304 365,345 58,345"/>
    <text class="weight" x="12" y="330">150g</text>
    <text class="flavour" x="355" y="329">Beetroot Flavor</text>
  </svg>

</div>
</body>
</html>
```